New Electrical Business Card Design

I would like a new design for my business cards.
i would like the same logo and font but new design
Please see attached files for front and back design.
large image can be used for graphics.
I would like the instagram link incorporated to back of card.
website site address needs to be changed to www.tidemarkelectrical.au
everything else stays as is

```html
<!DOCTYPE html>
<html lang="en">
<head>
<meta charset="utf-8">
<title>Tidemark Electrical &amp; Data – Business Cards</title>
<link href="https://fonts.googleapis.com/css2?family=Montserrat:wght@400;500;600;700;800&display=swap" rel="stylesheet">
<style>
  :root {
    --bg: #c4c4c4;
    --card: #f4f4f3;
    --ink: #2b2b2b;
    --ink-soft: #3d3d3d;
    --green: #1f9a4b;
    --rule: #3a3a3a;
  }
  * { box-sizing: border-box; margin: 0; padding: 0; }
  html, body { width: 1200px; height: 800px; overflow: hidden; }
  body {
    background: var(--bg);
    font-family: "Montserrat", sans-serif;
    color: var(--ink);
    position: relative;
  }
  .card {
    position: absolute;
    top: 340px;
    width: 480px;
    height: 274px;
    background: var(--card);
    overflow: hidden;
  }
  .card--front { left: 97px; }
  .card--back { left: 614px; }

  /* Front */
  .front-brand {
    position: absolute;
    left: 0; right: 0; top: 112px;
    text-align: center;
    font-weight: 800;
    font-size: 30px;
    letter-spacing: 1px;
    color: var(--ink);
  }
  .front-brand .brand-dot {
    display: inline-block;
    width: 12px; height: 12px;
    border-radius: 50%;
    background: var(--green);
    margin-right: 10px;
    vertical-align: 4px;
  }
  .services {
    position: absolute;
    left: 0; right: 0; top: 214px;
    text-align: center;
    font-weight: 600;
    font-size: 16.5px;
    letter-spacing: -0.4px;
    color: var(--ink-soft);
  }
  .services .sep { color: var(--green); margin: 0 4px; }

  /* Back */
  .back-brand {
    position: absolute;
    right: 48px; top: 64px;
    font-weight: 800;
    font-size: 16px;
    letter-spacing: 0.5px;
    color: var(--ink);
  }
  .holder-name {
    position: absolute;
    left: 26px; top: 134px;
    font-weight: 700;
    font-size: 22px;
    letter-spacing: -0.3px;
    color: var(--green);
  }
  .holder-role {
    position: absolute;
    left: 24px; top: 169px;
    font-size: 13.5px;
    color: var(--ink-soft);
  }
  .divider {
    position: absolute;
    left: 24px; right: 28px; top: 191px;
    height: 1.5px;
    background: var(--rule);
  }
  .contacts {
    position: absolute;
    left: 24px; top: 198px;
    list-style: none;
  }
  .contacts li {
    display: flex;
    align-items: center;
    height: 20px;
    font-size: 13px;
    color: var(--ink-soft);
  }
  .contacts svg { width: 11px; height: 11px; margin-right: 13px; fill: var(--green); }
  .registration {
    position: absolute;
    right: 30px; top: 212px;
    text-align: right;
    font-size: 13px;
    line-height: 19px;
    color: var(--ink-soft);
  }
  .footer-band { position: absolute; left: 0; bottom: 0; width: 480px; height: 22px; }
  .social {
    position: absolute;
    right: 24px; bottom: 3px;
    display: flex; align-items: center;
    font-size: 13px;
    color: #fff;
  }
  .social .social-mark {
    width: 10px; height: 10px;
    border: 1.5px solid #fff;
    margin-right: 5px;
  }
</style>
</head>
<body>
  <section class="card card--front">
    <div class="front-brand"><span class="brand-dot"></span>TIDEMARK ELECTRICAL</div>
    <p class="services">Residential <span class="sep">•</span> Commercial <span class="sep">•</span> Industrial <span class="sep">•</span> 24hrsservice</p>
  </section>

  <section class="card card--back">
    <div class="back-brand">TIDEMARK ELECTRICAL</div>
    <h1 class="holder-name">DANIEL HARROW</h1>
    <p class="holder-role">Managing Director</p>
    <div class="divider"></div>
    <ul class="contacts">
      <li><svg viewBox="0 0 24 24"><path d="M6.6 10.8a15.1 15.1 0 0 0 6.6 6.6l2.2-2.2a1 1 0 0 1 1-.25 11.4 11.4 0 0 0 3.6.57 1 1 0 0 1 1 1V20a1 1 0 0 1-1 1A17 17 0 0 1 3 4a1 1 0 0 1 1-1h3.5a1 1 0 0 1 1 1c0 1.25.2 2.45.57 3.57a1 1 0 0 1-.25 1z"/></svg>0400 318 772</li>
      <li><svg viewBox="0 0 24 24"><path d="M2 5h20v14H2z M3 6l9 7 9-7" stroke="#f4f4f3" stroke-width="1.5"/></svg>info@tidemarkelectrical.au</li>
      <li><svg viewBox="0 0 24 24"><circle cx="12" cy="12" r="10"/><path d="M2 12h20M12 2c3 3 3 17 0 20M12 2c-3 3-3 17 0 20" stroke="#f4f4f3" stroke-width="1.5" fill="none"/></svg>www.tidemarkelectrical.au</li>
    </ul>
    <p class="registration">ABN - 61 482 907 315<br>Lic number - 507164C</p>
    <svg class="footer-band" viewBox="0 0 480 22" preserveAspectRatio="none">
      <polygon points="0,6 274,6 270,13 0,13" fill="#3a3a3a"/>
      <polygon points="0,16 265,16 285,0 480,0 480,22 0,22" fill="#1f9a4b"/>
    </svg>
    <div class="social"><span class="social-mark"></span>tidemark.electrical</div>
  </section>
</body>
</html>
```